New Packaging Design for Olives

We are looking for a new packaging design for our product.
- Clear plastic cup container
- 90mm round lid and tapers down to 45mm base
- We do not want a box
- We would like a cardboard wrap around.
Product:
- Pitted Kalamata Olives
- 90g Net
We would like to product to be displayed from top view and side view.
We would like an image of kalamata olives on the packaging
our logo to appear on top and side
the bottom of the packaging to have room for a bar code, ingredients & nutritional panel.
This product is designed to target the accommodation/hotel market and we are wanting a classy looking design to attract mini bar customers.
Attached is an image of the cup & an internal mock up and our company logo.
We need a design that will seamlessly work across a variety of products including salsa, chilli sauce, tomato sauce and others.
Hotel Mini bar at 4 to 5 star hotels
Hotel

```html
<!DOCTYPE html>
<html lang="en">
<head>
<meta charset="utf-8">
<title>Bramwell Pitted Kalamata Olives – Wrap Label</title>
<link rel="stylesheet" href="https://fonts.googleapis.com/css2?family=IM+Fell+English&display=swap">
<style>
  :root {
    --ink-black: #1f1e1e;
    --logo-plate: #2b2b2b;
    --logo-yellow: #f4ec1c;
    --olive-band: #7e8b3a;
    --sage-field: #7b9c99;
    --sage-glow: #a3bcb8;
    --pale-band: #d4db8e;
    --base-band: #8fa042;
    --text-brown: #5a4037;
    --illus-dark: #4a2f38;
    --illus-leaf: #8fa64a;
  }
  * { margin: 0; padding: 0; box-sizing: border-box; }
  html, body { width: 1200px; height: 1199px; overflow: hidden; background: #ffffff; }
  .label {
    position: relative;
    width: 1200px;
    height: 1199px;
    font-family: "IM Fell English", Georgia, serif;
  }
  .brand-bar {
    position: absolute; left: 0; top: 0; width: 1200px; height: 252px;
    background: var(--ink-black);
  }
  .brand-plate {
    position: absolute; left: 330px; top: 46px; width: 540px; height: 160px;
    background: var(--logo-plate);
    display: flex; align-items: center; justify-content: center;
  }
  .brand-name {
    color: var(--logo-yellow);
    font-size: 122px;
    line-height: 1;
    letter-spacing: 1px;
  }
  .accent-stripe {
    position: absolute; left: 0; top: 252px; width: 1200px; height: 42px;
    background: var(--olive-band);
  }
  .hero-field {
    position: absolute; left: 0; top: 294px; width: 1200px; height: 572px;
    background: radial-gradient(ellipse 60% 55% at 52% 60%, var(--sage-glow) 0%, var(--sage-field) 70%);
  }
  .hero-illustration {
    position: absolute; left: 264px; top: 198px; width: 676px; height: 282px;
    border-radius: 18px;
    background: linear-gradient(180deg, var(--illus-dark) 0%, var(--illus-dark) 55%, var(--illus-leaf) 100%);
  }
  .product-band {
    position: absolute; left: 0; top: 866px; width: 1200px; height: 160px;
    background: var(--pale-band);
    display: flex; align-items: center; justify-content: center;
  }
  .product-name {
    color: var(--text-brown);
    font-size: 90px;
    font-weight: 400;
    line-height: 1;
    letter-spacing: 2px;
  }
  .weight-band {
    position: absolute; left: 0; top: 1026px; width: 1200px; height: 173px;
    background: var(--base-band);
    display: flex; align-items: center; justify-content: center;
  }
  .net-weight {
    color: var(--text-brown);
    font-size: 68px;
    line-height: 1;
    font-variant-numeric: lining-nums;
    margin-top: -16px;
  }
</style>
</head>
<body>
  <main class="label">
    <header class="brand-bar">
      <div class="brand-plate">
        <span class="brand-name">Bramwell</span>
      </div>
    </header>
    <div class="accent-stripe"></div>
    <section class="hero-field">
      <div class="hero-illustration" role="img" aria-label="Illustration of three glossy dark Kalamata olives resting on green olive leaves on a small white plate"></div>
    </section>
    <section class="product-band">
      <h1 class="product-name">Pitted Kalamata Olives</h1>
    </section>
    <footer class="weight-band">
      <p class="net-weight">90g Net</p>
    </footer>
  </main>
</body>
</html>
```